Business Card Design for a Sound engineer and DJ

We would like a residn of the business card.

Logo must remain the same.
The card is for the owner of the company.
The business card is in Arabic as the company is based in Kuwait.
The company specializes in sound engineering for singers concerts and events and in addition DJ.
The color options is up to the designer but we would like it masculine as the owner is a man.

Target Market(s)

All ages

Industry/Entity Type

Media

Contact Information for Business Card

Name:
Eng. Faisal Barrak
م/فيصل براك

The name above is in Arabic and English.

Title: General Manager
Mobile: +965 96370482
Office: +965 22480637
Email: info@qamarwave.net

Address:
Office no. 3
1st floor
Marjan Complex
Hamad Faraj St.
Salmiya
Kuwait

Instagram: @qamarwave
Snap: qamarwave

Requirements
Nice to have
• can we have Instagram icon and snap icon and a phone vector and email?
• Instead of writing the words

```html
<!DOCTYPE html>
<html lang="en">
<head>
<meta charset="utf-8">
<title>Qamarwave Business Card</title>
<link rel="stylesheet" href="https://fonts.googleapis.com/css2?family=Open+Sans:wght@400;600;700&family=Cairo:wght@600&display=swap">
<style>
  :root{
    --page:#1c1c1e;
    --card:#050505;
    --purple:#8b3fb0;
    --violet:#a35bd0;
    --sky:#5fc2ee;
  }
  *{box-sizing:border-box;margin:0;padding:0}
  html,body{width:1200px;height:900px;overflow:hidden;background:var(--page);font-family:"Open Sans",sans-serif}
  .sheet{position:relative;width:1200px;height:900px}
  .card{position:absolute;left:250px;width:700px;height:400px;background:var(--card);border-radius:22px;overflow:hidden}
  .card--front{top:35px}
  .card--back{top:465px}
  .swoosh{position:absolute;inset:0;width:700px;height:400px}

  .brand{position:absolute;display:flex;flex-direction:column;align-items:flex-start}
  .brand__name{display:flex;align-items:center;gap:12px;font-weight:600;color:var(--violet);letter-spacing:6px}
  .brand__mark{width:14px;height:14px;background:var(--violet)}
  .brand__tag{font-weight:600;color:var(--violet);letter-spacing:2px;font-size:12px;margin-top:6px}
  .brand__tag-ar{font-family:"Cairo",sans-serif;font-weight:600;color:var(--violet);font-size:14px;direction:rtl;line-height:1.3}

  .card--front .brand{left:238px;top:118px}
  .card--front .brand__name{font-size:30px}
  .handles{position:absolute;left:240px;top:214px;list-style:none;color:#fff;font-size:15px;line-height:22px}
  .handles li{display:flex;align-items:center;gap:8px}
  .handles .dot{width:10px;height:10px;background:var(--sky);border-radius:2px}
  .handles .dot--round{border-radius:50%}

  .tab{position:absolute;right:0;top:0;width:26px;height:78px;background:var(--sky);border-bottom-left-radius:14px}

  .person{position:absolute;right:58px;top:42px;text-align:right}
  .person__ar{font-family:"Cairo",sans-serif;font-weight:600;font-size:44px;line-height:1.1;color:var(--violet);direction:rtl}
  .person__en{font-weight:700;font-size:28px;color:var(--purple);line-height:1.15}
  .person__role{font-size:16px;color:var(--sky);margin-top:2px}

  .rule{position:absolute;left:320px;right:58px;top:200px;height:1px;background:var(--purple)}

  .card--back .brand{left:52px;top:186px}
  .card--back .brand__name{font-size:26px}

  .contacts{position:absolute;right:40px;top:208px;list-style:none;text-align:right;color:var(--violet);font-size:16px;line-height:22px}
  .contacts li{display:flex;justify-content:flex-end;align-items:center;gap:8px}
  .contacts svg{width:13px;height:13px;fill:none;stroke:var(--sky);stroke-width:1.8}

  .address{position:absolute;left:56px;top:290px;color:var(--violet);font-size:17px;line-height:22px;font-style:normal}
</style>
</head>
<body>
<main class="sheet">

  <section class="card card--front" aria-label="Card front">
    <svg class="swoosh" viewBox="0 0 700 400" aria-hidden="true">
      <path fill="var(--sky)" d="M0,352 C250,334 480,286 700,244 L700,260 C480,304 250,352 0,370 Z"/>
      <path fill="var(--purple)" d="M0,370 C250,352 480,304 700,260 L700,270 C500,330 330,380 250,400 L0,400 Z"/>
    </svg>
    <div class="brand">
      <div class="brand__name"><span class="brand__mark"></span>QAMARWAVE</div>
      <div class="brand__tag">DJ - SOUND ENG. - LIGHTING</div>
      <div class="brand__tag-ar">دي جي - هندسة صوت - إضاءة</div>
    </div>
    <ul class="handles">
      <li><span class="dot"></span>@qamarwave</li>
      <li><span class="dot dot--round"></span>qamarwave</li>
    </ul>
  </section>

  <section class="card card--back" aria-label="Card back">
    <svg class="swoosh" viewBox="0 0 700 400" aria-hidden="true">
      <path fill="var(--purple)" d="M330,400 C470,350 590,304 700,286 L700,400 Z"/>
      <path fill="var(--sky)" d="M305,400 C460,338 580,290 700,266 L700,286 C590,304 470,350 330,400 Z"/>
    </svg>
    <div class="tab"></div>

    <div class="person">
      <div class="person__ar">م/فيصل براك</div>
      <div class="person__en">Eng. Faisal Barrak</div>
      <div class="person__role">General Manager</div>
    </div>

    <div class="rule"></div>

    <div class="brand">
      <div class="brand__name"><span class="brand__mark"></span>QAMARWAVE</div>
      <div class="brand__tag">DJ - SOUND ENG. - LIGHTING</div>
      <div class="brand__tag-ar">دي جي - هندسة صوت - إضاءة</div>
    </div>

    <ul class="contacts">
      <li>+965 96370482
        <svg viewBox="0 0 14 14"><rect x="3.5" y="1" width="7" height="12" rx="1.2"/><line x1="6" y1="11" x2="8" y2="11"/></svg></li>
      <li>+965 22480637
        <svg viewBox="0 0 14 14"><path d="M3 1.5 L5.5 1.5 L6.5 4.5 L5 5.8 C5.8 7.6 6.6 8.4 8.2 9 L9.5 7.5 L12.5 8.5 L12.5 11 C12.5 12 11.6 12.6 10.6 12.5 C5.5 12 2 8.5 1.5 3.4 C1.4 2.4 2 1.5 3 1.5 Z"/></svg></li>
      <li>info@qamarwave.net
        <svg viewBox="0 0 14 14"><rect x="1" y="3" width="12" height="8.5" rx="1"/><path d="M1.5 3.5 L7 8 L12.5 3.5"/></svg></li>
    </ul>

    <address class="address">
      Office no. 3<br>
      1st floor Marjan Complex<br>
      Hamad Faraj St. Salmiya Kuwait
    </address>
  </section>

</main>
</body>
</html>
```